Quill And Ferry Business Card

I need a business card designed around my logo (which was designed here on Sketch Forum!)

Target Market(s)

Professional Businesses

Industry/Entity Type

Business

Requirements
Must have
• Details that must be on the business card:

Renata Ovalle
Director
0491 253 608
renata@quillandferry.com.au
www.quillandferry.com.au
PO Box 4720 Ashgrove Vale Vic 3094

```html
<!DOCTYPE html>
<html lang="en">
<head>
<meta charset="utf-8">
<title>Quill And Ferry – Business Card</title>
<link href="https://fonts.googleapis.com/css2?family=Cinzel:wght@400&family=Libre+Baskerville:wght@700&family=Tinos:wght@700&display=swap" rel="stylesheet">
<style>
  :root {
    --backdrop: #4a2c1c;
    --front-top: #e3e9c9;
    --front-mid: #fbfcf6;
    --front-low: #dfe2c3;
    --front-bottom: #b6b39c;
    --brand-dark: #2b2b2b;
    --brand-red: #c8202a;
    --card-white: #ffffff;
    --tan: #c49a6c;
    --tan-light: #c4b49c;
    --ink: #111111;
  }
  * { margin: 0; padding: 0; box-sizing: border-box; }
  html, body { width: 1200px; height: 1200px; overflow: hidden; }
  body { background: var(--backdrop); position: relative; }

  .card {
    position: absolute;
    left: 158px;
    width: 802px;
    height: 486px;
    border-radius: 24px;
    overflow: hidden;
  }

  /* Front */
  .card-front {
    top: 114px;
    background: linear-gradient(to bottom,
      var(--front-top) 0%,
      var(--front-mid) 49%,
      var(--front-low) 53%,
      var(--front-low) 70%,
      var(--front-bottom) 100%);
  }
  .brand-mark {
    position: absolute;
    left: 70px;
    top: 188px;
    width: 96px;
    height: 96px;
    border-radius: 50%;
    background: var(--brand-red);
  }
  .brand-name {
    position: absolute;
    left: 256px;
    top: 186px;
    font-family: "Cinzel", serif;
    font-weight: 400;
    font-size: 54px;
    line-height: 1;
    color: var(--brand-dark);
    white-space: nowrap;
  }
  .brand-tagline {
    position: absolute;
    left: 258px;
    top: 245px;
    font-family: "Cinzel", serif;
    font-size: 22px;
    letter-spacing: 7.5px;
    line-height: 1;
    color: var(--brand-red);
    white-space: nowrap;
  }

  /* Back */
  .card-back {
    top: 652px;
    background: var(--card-white);
  }
  .card-back svg { position: absolute; left: 0; top: 0; }
  .holder-name, .holder-role, .contact {
    position: absolute;
    color: var(--ink);
    white-space: nowrap;
    line-height: 1;
    transform-origin: left top;
  }
  .holder-name {
    left: 68px;
    top: 110px;
    font-family: "Libre Baskerville", serif;
    font-weight: 700;
    font-size: 56px;
  }
  .holder-role {
    left: 140px;
    top: 164px;
    font-family: "Libre Baskerville", serif;
    font-weight: 700;
    font-size: 56px;
  }
  .contact { font-weight: 700; }
  .contact-phone {
    left: 216px; top: 272px;
    font-family: "Libre Baskerville", serif;
    font-size: 38px;
  }
  .contact-email {
    left: 224px; top: 312px;
    font-family: "Tinos", serif;
    font-size: 44px;
    letter-spacing: -1px;
    transform: scaleX(0.84);
  }
  .contact-web {
    left: 224px; top: 361px;
    font-family: "Libre Baskerville", serif;
    font-size: 38px;
  }
  .contact-post {
    left: 226px; top: 406px;
    font-family: "Tinos", serif;
    font-size: 34px;
  }
</style>
</head>
<body>

  <section class="card card-front">
    <span class="brand-mark"></span>
    <div class="brand-name">QUILL AND FERRY</div>
    <div class="brand-tagline">LEDGERS KEPT SIMPLE</div>
  </section>

  <section class="card card-back">
    <svg width="802" height="486" viewBox="0 0 802 486" aria-hidden="true">
      <circle cx="150" cy="240" r="268" fill="var(--tan-light)"/>
      <circle cx="110" cy="240" r="250" fill="var(--tan)"/>
    </svg>
    <div class="holder-name">Renata Ovalle</div>
    <div class="holder-role">Director</div>
    <div class="contact contact-phone">Tell: 0491 253 608</div>
    <div class="contact contact-email">Email:renata@quillandferry.com.au</div>
    <div class="contact contact-web">www.quillandferry.com.au</div>
    <div class="contact contact-post">PO Box 4720 Ashgrove Vale Vic 3094</div>
  </section>

</body>
</html>
```